Poster / Flyer / Advertisement for Frosk Brew Chill (Unique Product!)

We’re selling alcoholic (7.5%) flavored ice for beer…for example, you might try our Lime flavor in a Valdor. We need a great ad/poster…please follow these guidelines:
USE THE PRODUCT PHOTO & KEEP IT SIMPLE!
Use the attached “action shot” of our product prominently. I prefer just the glass of beer, so turn off the layer with the beer bottle. Photoshop in a great background and KEEP IT SIMPLE - the product shot pretty much says it all. Find a great background, add the words “Your beer is getting warm”, and layer in some of our branding (see below). That’s it! Don’t make the poster too busy!
USE OUR CURRENT BRANDING
I’ve attached AI files with all of our branding. Layer in the pattern used on the packaging, our logo, and probably the “Frosk Chill” banner. Also, given that our most popular flavor is Lime in a Valdor, I would look for a background that helps express that (just a thought, it’s up to you to make it look good!).
MAKE IT VERSATILE
We need this to be versatile and easily scale up or down in size for various applications such as:
1) Large format poster for the front window of a convenience store
2) Smaller format for poster ads in bars/restaurants
3) Even smaller format for window clings that go on the glass doors of beer coolers
I also want the words for the poster to be easily changeable for the different applications:
1) Bar – I would use the tagline “Your beer is getting warm”
2) Convenience Store – I would use the line “Don’t drink warm beer…check the freezer!” or something similar. Just need it easy to change
Updates
Project Deadline Extended
Reason: Still deciding on designs. Need time to review with business partners. Thanks all!
Target Market(s)
Beer drinkers - especially those that like fruity beers like summer shandy
Industry/Entity Type
Brewery
Font styles to use
Other font styles liked:
- Use attached fonts!
Colors
Designer to choose colors to be used in the design.
Requirements
Must have
- Use the product shot and our branding...and a simple design!
Nice to have
- Want a "drinking an ice cold beer on a summer day" feel to this.

```html
<!DOCTYPE html>
<html lang="en">
<head>
<meta charset="utf-8">
<title>Frosk Brew Chill – Your beer is getting warm!</title>
<link rel="stylesheet" href="https://fonts.googleapis.com/css2?family=Oleo+Script:wght@400;700&family=Quicksand:wght@500;700&display=swap">
<style>
  :root {
    --green-deep: #3f8f12;
    --green-mid: #5cab1e;
    --green-bright: #8fd14f;
    --green-pale: #c6e7a6;
    --lime: #8ed94a;
    --ink: #1c1c1c;
    --paper: #ffffff;
    --lemon: #f2e600;
    --berry: #e8234a;
  }
  * { margin: 0; padding: 0; box-sizing: border-box; }
  html, body { width: 960px; height: 1200px; overflow: hidden; }
  .poster {
    position: relative;
    width: 960px;
    height: 1200px;
    overflow: hidden;
    background:
      repeating-conic-gradient(from 0deg at 30% 36%, rgba(255,255,255,.09) 0deg 7deg, rgba(255,255,255,0) 7deg 16deg),
      radial-gradient(circle at 30% 36%, var(--green-bright) 0%, var(--green-mid) 40%, var(--green-deep) 100%);
    font-family: "Quicksand", sans-serif;
    color: var(--ink);
  }
  .bands { position: absolute; inset: 0; }
  .headline {
    position: absolute;
    left: 30px;
    top: 150px;
    width: 500px;
    font-family: "Oleo Script", cursive;
    font-weight: 700;
    font-size: 110px;
    line-height: 104px;
    text-align: center;
    color: var(--ink);
    transform: rotate(-15deg);
    text-shadow:
      4px 0 0 var(--paper), -4px 0 0 var(--paper),
      0 4px 0 var(--paper), 0 -4px 0 var(--paper),
      3px 3px 0 var(--paper), -3px -3px 0 var(--paper),
      3px -3px 0 var(--paper), -3px 3px 0 var(--paper),
      6px 7px 0 rgba(0,0,0,.25);
  }
  .headline .line-indent { display: block; padding-left: 90px; }
  .abv-note {
    position: absolute;
    left: 96px;
    top: 660px;
    font-size: 33px;
    font-weight: 500;
    letter-spacing: .5px;
    white-space: nowrap;
    transform: rotate(-17deg);
    transform-origin: left center;
  }
  .product-shot {
    position: absolute;
    left: 500px;
    top: 130px;
    width: 330px;
    height: 690px;
    border-radius: 40px 40px 60px 60px;
    background: linear-gradient(90deg, #d9ddd6 0%, #ffffff 35%, #f3f5f1 70%, #c9cec4 100%);
    box-shadow: 20px 20px 40px rgba(0,0,0,.15);
  }
  .brand-mark {
    position: absolute;
    left: 54px;
    top: 678px;
    width: 440px;
    height: 440px;
    border-radius: 50%;
    background: var(--ink);
    display: flex;
    align-items: center;
    justify-content: center;
    text-align: center;
  }
  .brand-mark span {
    font-family: "Oleo Script", cursive;
    font-weight: 700;
    font-size: 66px;
    line-height: 72px;
    color: var(--lime);
  }
  .flavours-lead {
    position: absolute;
    left: 520px;
    top: 952px;
    font-size: 46px;
    line-height: 48px;
    font-weight: 700;
    transform: rotate(-21deg);
    transform-origin: left bottom;
    white-space: nowrap;
  }
  .flavour {
    position: absolute;
    width: 124px;
    text-align: center;
  }
  .flavour .mark {
    width: 124px;
    height: 124px;
    border-radius: 50%;
    background: var(--ink);
    display: flex;
    align-items: center;
    justify-content: center;
    font-family: "Oleo Script", cursive;
    font-weight: 700;
    font-size: 30px;
  }
  .flavour .name {
    display: block;
    font-family: "Oleo Script", cursive;
    font-size: 26px;
    transform: rotate(-12deg);
    margin-top: 10px;
  }
  .flavour--lemon { left: 578px; top: 1000px; }
  .flavour--lemon .mark { color: var(--lemon); }
  .flavour--lemon .name { padding-left: 40px; }
  .flavour--strawberry { left: 746px; top: 956px; }
  .flavour--strawberry .mark { color: var(--berry); }
  .flavour--strawberry .name { padding-left: 30px; margin-top: 4px; }
  .ampersand {
    position: absolute;
    left: 704px;
    top: 1000px;
    font-size: 46px;
    font-weight: 700;
  }
</style>
</head>
<body>
<main class="poster">
  <svg class="bands" width="960" height="1200" viewBox="0 0 960 1200" aria-hidden="true">
    <polygon points="0,690 960,420 960,470 0,790" fill="var(--green-pale)" opacity=".85"/>
    <polygon points="0,780 960,465 960,830 0,1180" fill="var(--paper)"/>
    <polygon points="0,1100 960,760 960,840 0,1190" fill="var(--green-pale)"/>
    <polygon points="0,1170 960,815 960,1200 0,1200" fill="var(--green-mid)"/>
  </svg>

  <h1 class="headline">Your beer<br>is getting<br><span class="line-indent">warm!</span></h1>

  <p class="abv-note">contains 7.5 % alcohol</p>

  <div class="product-shot" role="img" aria-label="Stack of three white Frosk Chill lime ice cups, 7.5% alcohol, 3 x 100 ml"></div>

  <div class="brand-mark"><span>Frosk<br>Brew Chill</span></div>

  <p class="flavours-lead">also Available in</p>

  <div class="flavour flavour--lemon">
    <div class="mark">Frosk</div>
    <span class="name">Lemon</span>
  </div>
  <span class="ampersand">&amp;</span>
  <div class="flavour flavour--strawberry">
    <div class="mark">Frosk</div>
    <span class="name">Strawberry</span>
  </div>
</main>
</body>
</html>
```